Powerpoint template

I am looking for a brand based PPT template that can also be used as the basis for datasheet creation. I have attached a document with some of our branding structure in as an FYI to help.

To be clear I am looking a background design, bullets, layouts, different styles for differing content types. This is a template to be used for lots of presentations.
Updates

Project Deadline Extended
Reason: I have committed to the payment and wanted to give people chance to respond.

Target Market(s)

Enterprise

Requirements
Must have
• Brand standard. different page design choices for different content types
Nice to have
• brand font if it works. Use of some play on the logo in bullets
Should not have
• must be on brand and focused on the business audience

```html
<!DOCTYPE html>
<html lang="en">
<head>
<meta charset="utf-8">
<title>Vantiqa Presentation Template</title>
<link href="https://fonts.googleapis.com/css2?family=Ubuntu:wght@400;500&family=Arimo:wght@400&display=swap" rel="stylesheet">
<style>
  :root {
    --stage: #000000;
    --slide-bg: #f0f0f0;
    --brand-blue: #1a74c4;
    --brand-green: #7cc242;
    --footer-blue: #1b5f9e;
    --ink: #2a2a2a;
    --ink-soft: #444444;
    --rule: #c9c9c9;
    --decor: #e6e6e6;
  }
  * { margin: 0; padding: 0; box-sizing: border-box; }
  html, body { width: 1200px; height: 922px; overflow: hidden; background: var(--stage); }
  .board { position: relative; width: 1200px; height: 922px; }

  .slide {
    position: absolute; width: 569px; height: 427px;
    background: var(--slide-bg); overflow: hidden;
    font-family: "Arimo", Arial, sans-serif; color: var(--ink);
  }
  .slide--cover { left: 19px; top: 19px; }
  .slide--columns { left: 617px; top: 19px; }
  .slide--bullets { left: 19px; top: 473px; }
  .slide--closing { left: 617px; top: 473px; }

  /* footer */
  .footer-line { position: absolute; left: 0; bottom: 0; width: 100%; height: 5px; background: var(--brand-green); }
  .footer-tab {
    position: absolute; right: 0; bottom: 0; width: 184px; height: 19px;
    background: var(--footer-blue);
    clip-path: polygon(10px 0, 100% 0, 100% 100%, 0 100%);
    color: #fff; font-size: 10px; letter-spacing: 1.6px;
    line-height: 19px; text-align: right; padding-right: 10px;
  }

  /* wordmark stand-in */
  .wordmark { position: absolute; display: flex; align-items: center; gap: 6px; }
  .wordmark-dot { border-radius: 50%; background: var(--brand-green); flex: none; }
  .wordmark-name { font-family: "Ubuntu", sans-serif; font-weight: 400; color: var(--brand-blue); }

  /* cover */
  .cover-mark { left: 0; width: 100%; top: 138px; justify-content: center; }
  .cover-mark .wordmark-dot { width: 30px; height: 30px; }
  .cover-mark .wordmark-name { font-size: 40px; }
  .cover-title {
    position: absolute; top: 234px; width: 100%; text-align: center;
    font-family: "Ubuntu", sans-serif; font-weight: 500; font-size: 26px; color: var(--brand-blue);
  }
  .cover-subtext {
    position: absolute; top: 276px; width: 100%; text-align: center;
    font-size: 11px; line-height: 16px; color: var(--ink);
  }

  /* content header */
  .slide-header { position: absolute; left: 0; top: 0; width: 100%; height: 60px; }
  .slide-title {
    position: absolute; left: 16px; top: 15px;
    font-family: "Ubuntu", sans-serif; font-weight: 400; font-size: 22px; color: var(--brand-blue);
  }
  .slide-title .accent { color: var(--brand-green); }
  .header-mark { right: 6px; top: 16px; }
  .header-mark .wordmark-dot { width: 16px; height: 16px; }
  .header-mark .wordmark-name { font-size: 24px; }
  .header-rule {
    position: absolute; left: 0; top: 57px; width: 100%; height: 3px;
    border-top: 1px solid var(--brand-blue); border-bottom: 1px solid var(--brand-green);
  }

  /* two-column copy */
  .copy-column { position: absolute; top: 91px; width: 230px; font-size: 8.5px; line-height: 15.6px; color: var(--ink); }
  .copy-column--left { left: 34px; }
  .copy-column--right { left: 291px; }
  .copy-column p + p { margin-top: 15.6px; }

  /* bullet list */
  .bullet-list { position: absolute; left: 38px; top: 104px; list-style: none; }
  .bullet-list li {
    display: flex; align-items: center; height: 32.8px;
    font-size: 11.5px; color: var(--ink);
  }
  .bullet-list svg { width: 10px; height: 12px; margin-right: 9px; flex: none; }

  /* closing */
  .closing-decor {
    position: absolute; left: -40px; top: -10px; width: 300px; height: 300px;
    border-radius: 50%; background: var(--decor);
  }
  .closing-title {
    position: absolute; top: 96px; left: 0; width: 660px; text-align: center;
    font-family: "Ubuntu", sans-serif; font-weight: 400; font-size: 23px; color: var(--brand-blue); letter-spacing: 0.3px;
  }
  .closing-mark { left: 100px; top: 193px; }
  .closing-mark .wordmark-dot { width: 30px; height: 30px; }
  .closing-mark .wordmark-name { font-size: 40px; }
  .closing-divider { position: absolute; left: 354px; top: 173px; width: 1px; height: 113px; background: var(--rule); }
  .contact { position: absolute; left: 375px; top: 184px; font-size: 10px; color: var(--ink-soft); }
  .contact-address { font-size: 11px; margin-bottom: 12px; }
  .contact-row { display: flex; align-items: center; height: 24px; font-size: 9.5px; }
  .contact-row svg { width: 12px; height: 12px; margin-right: 5px; }
</style>
</head>
<body>
<main class="board">

  <section class="slide slide--cover">
    <div class="wordmark cover-mark"><span class="wordmark-dot"></span><span class="wordmark-name">vantiqa</span></div>
    <h1 class="cover-title">Project Title Here</h1>
    <p class="cover-subtext">Subtext here Subtext here Subtext here<br>Subtext here Subtext here Subtext here<br>Subtext here Subtext here</p>
    <div class="footer-line"></div>
    <div class="footer-tab">www.vantiqa.com</div>
  </section>

  <section class="slide slide--columns">
    <header class="slide-header">
      <h2 class="slide-title">Project <span class="accent">Title Here</span></h2>
      <div class="wordmark header-mark"><span class="wordmark-dot"></span><span class="wordmark-name">vantiqa</span></div>
      <div class="header-rule"></div>
    </header>
    <div class="copy-column copy-column--left">
      <p>Subtext here Subtext here Subtext here Subtext here<br>Subtext here Subtext here Subtext here Subtext here<br>Subtext here Subtext here Subtext here Subtext here<br>Subtext here Subtext here Subtext here Subtext here<br>Subtext here Subtext here Subtext here Subtext here<br>Subtext here Subtext here Subtext here Subtext here<br>Subtext here Subtext here Subtext here Subtext here<br>Subtext here Subtext here Subtext here Subtext here</p>
      <p>Subtext here Subtext here Subtext here Subtext here<br>Subtext here Subtext here Subtext here Subtext here<br>Subtext here Subtext here Subtext here Subtext here<br>Subtext here Subtext here Subtext here Subtext here<br>Subtext here Subtext here Subtext here Subtext here<br>Subtext here Subtext here Subtext here Subtext here<br>Subtext here Subtext here Subtext here Subtext here<br>Subtext here Subtext here Subtext here Subtext here</p>
    </div>
    <div class="copy-column copy-column--right">
      <p>Subtext here Subtext here Subtext here Subtext here<br>Subtext here Subtext here Subtext here Subtext here<br>Subtext here Subtext here Subtext here Subtext here<br>Subtext here Subtext here Subtext here Subtext here<br>Subtext here Subtext here Subtext here Subtext here<br>Subtext here Subtext here Subtext here Subtext here<br>Subtext here Subtext here Subtext here Subtext here<br>Subtext here Subtext here Subtext here Subtext here</p>
      <p>Subtext here Subtext here Subtext here Subtext here<br>Subtext here Subtext here Subtext here Subtext here<br>Subtext here Subtext here Subtext here Subtext here<br>Subtext here Subtext here Subtext here Subtext here<br>Subtext here Subtext here Subtext here Subtext here<br>Subtext here Subtext here Subtext here Subtext here<br>Subtext here Subtext here Subtext here Subtext here<br>Subtext here Subtext here Subtext here Subtext here</p>
    </div>
    <div class="footer-line"></div>
    <div class="footer-tab">www.vantiqa.com</div>
  </section>

  <section class="slide slide--bullets">
    <header class="slide-header">
      <h2 class="slide-title">Project <span class="accent">Title Here</span></h2>
      <div class="wordmark header-mark"><span class="wordmark-dot"></span><span class="wordmark-name">vantiqa</span></div>
      <div class="header-rule"></div>
    </header>
    <ul class="bullet-list">
      <li><svg viewBox="0 0 10 12"><path d="M1 1 L8 6 L1 11" fill="none" stroke="#7cc242" stroke-width="3"/></svg>Subtext here Subtext here Subtext here Subtext here Subtext here Subtext here Subtext here</li>
      <li><svg viewBox="0 0 10 12"><path d="M1 1 L8 6 L1 11" fill="none" stroke="#7cc242" stroke-width="3"/></svg>Subtext here Subtext here Subtext here Subtext here Subtext here Subtext here Subtext here</li>
      <li><svg viewBox="0 0 10 12"><path d="M1 1 L8 6 L1 11" fill="none" stroke="#7cc242" stroke-width="3"/></svg>Subtext here Subtext here Subtext here Subtext here Subtext here Subtext here Subtext here</li>
      <li><svg viewBox="0 0 10 12"><path d="M1 1 L8 6 L1 11" fill="none" stroke="#7cc242" stroke-width="3"/></svg>Subtext here Subtext here Subtext here Subtext here Subtext here Subtext here Subtext here</li>
      <li><svg viewBox="0 0 10 12"><path d="M1 1 L8 6 L1 11" fill="none" stroke="#7cc242" stroke-width="3"/></svg>Subtext here Subtext here Subtext here Subtext here Subtext here Subtext here Subtext here</li>
      <li><svg viewBox="0 0 10 12"><path d="M1 1 L8 6 L1 11" fill="none" stroke="#7cc242" stroke-width="3"/></svg>Subtext here Subtext here Subtext here Subtext here Subtext here Subtext here Subtext here</li>
      <li><svg viewBox="0 0 10 12"><path d="M1 1 L8 6 L1 11" fill="none" stroke="#7cc242" stroke-width="3"/></svg>Subtext here Subtext here Subtext here Subtext here Subtext here Subtext here Subtext here</li>
      <li><svg viewBox="0 0 10 12"><path d="M1 1 L8 6 L1 11" fill="none" stroke="#7cc242" stroke-width="3"/></svg>Subtext here Subtext here Subtext here Subtext here Subtext here Subtext here Subtext here</li>
    </ul>
    <div class="footer-line"></div>
    <div class="footer-tab">www.vantiqa.com</div>
  </section>

  <section class="slide slide--closing">
    <div class="closing-decor"></div>
    <h2 class="closing-title">THANKS FOR YOUR VALUABLE TIMES</h2>
    <div class="wordmark closing-mark"><span class="wordmark-dot"></span><span class="wordmark-name">vantiqa</span></div>
    <div class="closing-divider"></div>
    <address class="contact" style="font-style:normal">
      <div class="contact-address">Address Street 78</div>
      <div class="contact-row"><svg viewBox="0 0 12 12"><rect width="12" height="12" rx="1.5" fill="#444"/><path d="M4 3 Q3 6 4 9 L5.5 8 L5 6 L5.5 4 Z" fill="#fff"/></svg>+01.5550.1234</div>
      <div class="contact-row"><svg viewBox="0 0 12 12"><rect width="12" height="12" rx="1.5" fill="#444"/><rect x="3.5" y="2" width="5" height="8" rx="1" fill="#fff"/></svg>+0155.0199</div>
      <div class="contact-row"><svg viewBox="0 0 12 12"><rect y="1" width="12" height="10" rx="1.5" fill="#444"/><rect x="2" y="3" width="8" height="6" fill="#fff"/></svg>contact@email.com</div>
    </address>
    <div class="footer-line"></div>
    <div class="footer-tab">www.vantiqa.com</div>
  </section>

</main>
</body>
</html>
```